Business Card for beauty technology startup

Design Glowmi Business Card for a Beauty, based on the website identity and colors (https://www.glowmi-example.com).
Glowmi is a beauty tech startup that gathers helpful product info for beauty lovers and consumers (such as availability on stores, price range and product reviews) for makeup products. The card design must be young, colorful but clean, and very modern.

Target Market(s)

woman, 15-35

Industry/Entity Type

Cosmetics

Contact Information for Business Card

Full Name, address, phone

Font styles to use
Other font styles liked:
• Advent Pro

Colors
e34297
86cfc6
ffffff
5c5c5c
e8e8e8
e667a6
b2b2b2

Requirements
Must have
• One full colored side with a creative design and another with card info
• Use Color palette: #95C5C5 and/or #D38AA5
• Use fonts: Advent Pro
• Use website identity: https://www.glowmi-example.com
Nice to have
• If needed extra font: Roboto

```html
<!DOCTYPE html>
<html lang="en">
<head>
<meta charset="utf-8">
<title>Glowmi Business Card</title>
<link href="https://fonts.googleapis.com/css2?family=Advent+Pro:wght@300;400;500&display=swap" rel="stylesheet">
<style>
  :root {
    --backdrop: #4f706e;
    --card-white: #f4f5f5;
    --teal: #4e8f8c;
    --teal-light: #9cc8c6;
    --teal-deep: #6aa9a7;
    --ink: #2b2b2b;
    --ink-soft: #5c5c5c;
    --petal: #e4e9f0;
  }
  * { margin: 0; padding: 0; box-sizing: border-box; }
  html, body { width: 1200px; height: 900px; overflow: hidden; }
  body {
    background: var(--backdrop);
    font-family: "Advent Pro", sans-serif;
    position: relative;
  }
  .card { position: absolute; overflow: hidden; }

  /* Info side */
  .card-info {
    left: 218px; top: 171px; width: 319px; height: 558px;
    background: var(--card-white);
    color: var(--ink-soft);
    text-align: center;
  }
  .floral-area {
    position: absolute; left: 70px; top: 0; width: 249px; height: 213px;
    background: radial-gradient(ellipse at 75% 45%, #ffffff 0%, var(--petal) 40%, rgba(244,245,245,0) 72%);
  }
  .brand-lockup {
    position: absolute; left: 0; right: 0; top: 212px;
    display: flex; justify-content: center; align-items: center; gap: 8px;
  }
  .brand-dot {
    width: 14px; height: 14px; border-radius: 50%;
    border: 2px solid var(--teal);
  }
  .brand-name {
    font-size: 30px; font-weight: 400; color: var(--teal); letter-spacing: 1px;
  }
  .person-name {
    position: absolute; left: 0; right: 0; top: 293px;
    font-size: 22px; font-weight: 400; color: var(--ink); letter-spacing: 0.5px;
  }
  .person-title {
    position: absolute; left: 0; right: 0; top: 322px;
    font-size: 15px; font-weight: 400;
  }
  .divider {
    position: absolute; left: 50px; width: 218px; top: 357px;
    height: 2px; background: var(--teal);
  }
  .address {
    position: absolute; left: 0; right: 0; top: 379px;
    font-size: 15px; line-height: 18px;
  }
  .contact-icons {
    position: absolute; left: 0; right: 0; top: 436px;
    display: flex; justify-content: center; gap: 14px;
  }
  .contact-icons svg { width: 20px; height: 20px; }
  .contact-lines {
    position: absolute; left: 0; right: 0; top: 473px;
    font-size: 16px; line-height: 18.5px;
  }
  .contact-lines .accent { color: var(--teal); }

  /* Colour side */
  .card-brand {
    left: 558px; top: 450px; width: 503px; height: 277px;
    background: linear-gradient(100deg, var(--teal-light) 0%, #8ec0bf 55%, var(--teal-deep) 100%);
    display: flex; align-items: center; justify-content: center; gap: 26px;
  }
  .brand-ring {
    width: 70px; height: 70px; border-radius: 50%;
    border: 2.5px solid #f2f6f6;
  }
  .brand-wordmark {
    font-size: 60px; font-weight: 300; color: #f2f6f6;
    letter-spacing: 9px; text-transform: uppercase;
  }
</style>
</head>
<body>
  <section class="card card-info">
    <div class="floral-area" role="img" aria-label="Soft pale watercolour flower with drifting petals"></div>
    <div class="brand-lockup">
      <span class="brand-dot"></span>
      <span class="brand-name">Glowmi</span>
    </div>
    <h1 class="person-name">MARISOL AVERY</h1>
    <p class="person-title">Managing Director</p>
    <div class="divider"></div>
    <p class="address">418 Coral Bay Ave<br>Palm Harbor, Florida 34683</p>
    <div class="contact-icons">
      <svg viewBox="0 0 20 20" aria-label="Phone"><circle cx="10" cy="10" r="10" fill="var(--teal)"/><path d="M6 8.5c0-1.5 1.8-2.5 4-2.5s4 1 4 2.5l-1.5.5-.6-1.3H8.1L7.5 9z M7 10h6l1 3.5H6z" fill="#fff"/></svg>
      <svg viewBox="0 0 20 20" aria-label="Email"><circle cx="10" cy="10" r="10" fill="var(--teal)"/><rect x="5.5" y="6.8" width="9" height="6.4" fill="#fff"/><path d="M5.5 7l4.5 3.6L14.5 7" fill="none" stroke="var(--teal)" stroke-width="1"/></svg>
      <svg viewBox="0 0 20 20" aria-label="Website"><circle cx="10" cy="10" r="10" fill="var(--teal)"/><g fill="none" stroke="#fff" stroke-width="1.4" stroke-linecap="round"><path d="M9 11l-1.6 1.6a1.6 1.6 0 0 1-2.3-2.3L6.7 8.7"/><path d="M11 9l1.6-1.6a1.6 1.6 0 0 1 2.3 2.3l-1.6 1.6"/><path d="M8.3 11.7l3.4-3.4"/></g></svg>
    </div>
    <p class="contact-lines">555-218-7730<br>hello@glowmi-example.com<br>www.<span class="accent">glowmi-example</span>.com</p>
  </section>

  <section class="card card-brand">
    <span class="brand-ring"></span>
    <span class="brand-wordmark">Glowmi</span>
  </section>
</body>
</html>
```